Brochure

I have a current booklet for Brightwater Labs, I need to incorporate additional information and testing into it. attached are the current inside pages and the additional items that need to be added.

Requirements
Must have
• matching the background, colors, and format of the original inside booklet pages.

```html
<!DOCTYPE html>
<html lang="en">
<head>
<meta charset="utf-8">
<title>Brightwater Labs – Test Panels</title>
<link href="https://fonts.googleapis.com/css2?family=Montserrat:wght@700;800&family=Source+Sans+3:wght@400;600&display=swap" rel="stylesheet">
<style>
  :root{
    --board:#231f20;
    --paper:#ffffff;
    --brand:#1779c1;
    --brand-deep:#2a5f9e;
    --brand-light:#6aa6dc;
    --ink:#333;
    --muted:#4a4a4a;
    --rule:#c9c9c9;
  }
  *{box-sizing:border-box;margin:0;padding:0}
  html,body{width:1044px;height:1200px;overflow:hidden;background:var(--board)}
  .board{position:absolute;left:0;top:0;width:1792px;height:2060px;transform:scale(.58259);transform-origin:0 0;background:var(--board)}
  .page{position:absolute;width:696px;height:850px;background:var(--paper);overflow:hidden;font-family:"Source Sans 3",sans-serif;color:var(--ink)}
  .page--nail{left:171px;top:151px}
  .page--abr{left:925px;top:151px}
  .page--uti{left:171px;top:1058px}
  .page--wound{left:925px;top:1058px}
  .page__title{position:absolute;left:119px;top:66px;font-family:"Montserrat",sans-serif;font-weight:800;font-size:32px;letter-spacing:.3px;color:var(--brand);white-space:nowrap}
  .page__count{position:absolute;left:119px;top:119px;font-family:"Montserrat",sans-serif;font-weight:800;font-size:13.5px;color:var(--muted)}
  .page__intro{position:absolute;left:119px;top:138px;width:470px;font-size:15px;line-height:22px;color:var(--muted)}
  .benefits{position:absolute;left:119px;top:209px;list-style:none}
  .benefit{display:flex;align-items:center;height:34.5px;font-size:12.5px;color:var(--ink)}
  .benefit svg{width:27px;height:27px;margin-right:12px;flex:none}
  .panel{position:absolute;border-collapse:collapse;font-size:13px;color:var(--ink)}
  .panel th{background:var(--brand);color:#fff;text-align:left;font-family:"Montserrat",sans-serif;font-weight:800;font-size:13px;height:27px;padding:0 20px}
  .panel td{border:1px solid var(--rule);border-top:none;padding:0 20px;height:25.8px;white-space:nowrap}
  .panel--tight td{height:18.2px;line-height:17px}
  .panel--tight td.tall{height:36px;line-height:11px;white-space:normal}
  .panel--abr td{border-left:none;border-right:none}
  .panel--abr td:first-child{border-left:1px solid var(--rule);width:97px}
  .panel--abr td:nth-child(2){padding:0;width:42px}
  .panel--abr td:last-child{border-right:1px solid var(--rule);padding-left:0}
  .corner{position:absolute;left:0;bottom:0;width:696px;height:260px}
</style>
</head>
<body>
<svg width="0" height="0" style="position:absolute" aria-hidden="true">
  <defs>
    <linearGradient id="facetTone" x1="0" y1="0" x2="1" y2="1">
      <stop offset="0" stop-color="#2f5f97"/>
      <stop offset=".5" stop-color="#4b8ad0"/>
      <stop offset="1" stop-color="#9cc6ee"/>
    </linearGradient>
    <symbol id="ico-dollar" viewBox="0 0 26 26"><circle cx="13" cy="13" r="13" fill="#1779c1"/><text x="13" y="19" text-anchor="middle" font-family="Montserrat,sans-serif" font-weight="800" font-size="17" fill="#fff">$</text></symbol>
    <symbol id="ico-timer" viewBox="0 0 26 26"><circle cx="13" cy="13" r="13" fill="#1779c1"/><circle cx="13" cy="14" r="6.5" fill="none" stroke="#fff" stroke-width="1.4"/><path d="M13 14V10.5M11.5 6.5h3" stroke="#fff" stroke-width="1.4" fill="none"/></symbol>
    <symbol id="ico-gear" viewBox="0 0 26 26"><circle cx="13" cy="13" r="13" fill="#1779c1"/><circle cx="13" cy="13" r="7" fill="none" stroke="#fff" stroke-width="1.6" stroke-dasharray="2.5 1.5"/><circle cx="13" cy="13" r="3" fill="none" stroke="#fff" stroke-width="1.4"/></symbol>
    <symbol id="ico-chart" viewBox="0 0 26 26"><circle cx="13" cy="13" r="13" fill="#1779c1"/><path d="M7 19h12M8.5 19v-3M11.5 19v-5M14.5 19v-6M17.5 19v-8M8 13l4-3 3 1 4-4" stroke="#fff" stroke-width="1.3" fill="none"/></symbol>
  </defs>
</svg>

<main class="board">

  <!-- Nail / Fungal -->
  <section class="page page--nail">
    <h2 class="page__title">NAIL / FUNGAL</h2>
    <p class="page__count">18 TARGETS</p>
    <p class="page__intro">A provider’s #1 priority is their patients. When you bring them more targets, you are providing them better tools for treatment</p>
    <ul class="benefits">
      <li class="benefit"><svg><use href="#ico-dollar"/></svg>Cost effective to help maximize your lab’s profits</li>
      <li class="benefit"><svg><use href="#ico-timer"/></svg>&lt;45 minute run time ensures faster turnaround times</li>
      <li class="benefit"><svg><use href="#ico-gear"/></svg>Compatible with ALL PCR MACHINES</li>
      <li class="benefit"><svg><use href="#ico-chart"/></svg>Highly demanded targets to make your lab more appealing to providers</li>
    </ul>
    <table class="panel" style="left:119px;top:370px;width:214px">
      <tr><th>FUNGI</th></tr>
      <tr><td>Microsporum gypseum</td></tr><tr><td>Microsporum canis/ audouinii</td></tr><tr><td>Trichophyton spp</td></tr><tr><td>Malassezia furfur</td></tr><tr><td>Malassezia sympodialis</td></tr><tr><td>Candida krusei</td></tr><tr><td>Candida albicans</td></tr><tr><td>Candida glabrata</td></tr><tr><td>Candida parapsilosis</td></tr>
    </table>
    <table class="panel" style="left:364px;top:370px;width:214px">
      <tr><th>FUNGI</th></tr>
      <tr><td>Candida auris</td></tr><tr><td>Aspergillus niger</td></tr><tr><td>Aspergillus flavus</td></tr><tr><td>Aspergillus fumigatus</td></tr><tr><td>Aspergillus terreus</td></tr><tr><td>Epidermophyton floccosum</td></tr><tr><td>Fusarium oxysporum</td></tr><tr><td>Trichosporon asahii</td></tr><tr><td>Trichosporon mucoides</td></tr>
    </table>
    <svg class="corner" viewBox="0 0 696 260"><polygon points="0,7 480,260 0,141" fill="url(#facetTone)" role="img" aria-label="Low-poly blue facet texture"/><polygon points="0,141 479,260 0,260" fill="#1779c1"/></svg>
  </section>

  <!-- Antibiotic Resistance Gene -->
  <section class="page page--abr">
    <h2 class="page__title">ANTIBIOTIC RESISTANCE GENE</h2>
    <p class="page__count">12 TARGETS</p>
    <p class="page__intro">A provider’s #1 priority is their patients. When you bring them more targets, you are providing them better tools for treatment.</p>
    <ul class="benefits">
      <li class="benefit"><svg><use href="#ico-dollar"/></svg>Cost effective to help maximize your lab’s profits</li>
      <li class="benefit"><svg><use href="#ico-timer"/></svg>&lt;45 minute run time ensures faster turnaround times</li>
      <li class="benefit"><svg><use href="#ico-gear"/></svg>Compatible with ALL PCR MACHINES</li>
      <li class="benefit"><svg><use href="#ico-chart"/></svg>Highly demanded targets to make your lab more appealing to providers</li>
    </ul>
    <table class="panel panel--abr" style="left:184px;top:370px;width:329px">
      <tr><th colspan="3">ABR</th></tr>
      <tr><td>KPC</td><td>–</td><td>Carbapenem resistance</td></tr>
      <tr><td>NDM</td><td>–</td><td>Carbapenem resistance</td></tr>
      <tr><td>VIM</td><td>–</td><td>Carbapenem resistance</td></tr>
      <tr><td>IMP</td><td>–</td><td>Carbapenem resistance</td></tr>
      <tr><td>qnr</td><td>–</td><td>Quinolone resistance</td></tr>
      <tr><td>vanB</td><td>–</td><td>Vancomycin resistance</td></tr>
      <tr><td>OXA-48</td><td>–</td><td>Carbapenem resistance</td></tr>
      <tr><td>mecA/mecC</td><td>–</td><td>Methicillin resistance</td></tr>
      <tr><td>CTX</td><td>–</td><td>M ESBL</td></tr>
      <tr><td>sul</td><td>–</td><td>Sulfonamide resistance</td></tr>
      <tr><td>vanA</td><td>–</td><td>Vancomycin resistance</td></tr>
      <tr><td>dfrA</td><td>–</td><td>Trimethoprim resistance</td></tr>
    </table>
    <svg class="corner" viewBox="0 0 696 260"><polygon points="0,7 480,260 0,141" fill="url(#facetTone)" role="img" aria-label="Low-poly blue facet texture"/><polygon points="0,141 479,260 0,260" fill="#1779c1"/></svg>
  </section>

  <!-- Urinary Tract Infection -->
  <section class="page page--uti">
    <h2 class="page__title">URINARY TRACT INFECTION</h2>
    <p class="page__count">28 TARGETS</p>
    <p class="page__intro">A provider’s #1 priority is their patients. When you bring them more targets, you are providing them better tools for treatment.</p>
    <ul class="benefits">
      <li class="benefit"><svg><use href="#ico-dollar"/></svg>Cost effective to help maximize your lab’s profits</li>
      <li class="benefit"><svg><use href="#ico-timer"/></svg>&lt;45 minute run time ensures faster turnaround times</li>
      <li class="benefit"><svg><use href="#ico-gear"/></svg>Compatible with ALL PCR MACHINES</li>
      <li class="benefit"><svg><use href="#ico-chart"/></svg>Highly demanded targets to make your lab more appealing to providers</li>
    </ul>
    <table class="panel panel--tight" style="left:119px;top:349px;width:214px">
      <tr><th>FUNGI</th></tr>
      <tr><td>Candida parapsilosis</td></tr><tr><td>Candida glabrata</td></tr><tr><td>Candida auris</td></tr><tr><td>Candida tropicalis</td></tr><tr><td>Candida krusei</td></tr><tr><td>Candida albicans</td></tr>
    </table>
    <table class="panel panel--tight" style="left:364px;top:349px;width:214px">
      <tr><th>BACTERIA</th></tr>
      <tr><td>Escherichia coli</td></tr><tr><td>Streptococcus agalactiae</td></tr><tr><td>Klebsiella oxytoca</td></tr><tr><td>Staphylococcus saprophyticus</td></tr><tr><td>Serratia marcescens</td></tr><tr><td>Proteus mirabilis</td></tr><tr><td>Aerococcus urinae</td></tr><tr><td>Treponema pallidum</td></tr><tr><td>Enterobacter cloacae</td></tr><tr><td>Pseudomonas aeruginosa</td></tr><tr><td>Citrobacter freundii</td></tr><tr><td>Klebsiella aerogenes</td></tr><tr><td>Klebsiella pneumoniae</td></tr><tr><td>Morganella morganii</td></tr><tr><td>Corynebacterium urealyticum</td></tr><tr><td>Enterococcus faecium</td></tr><tr><td>Enterococcus faecalis</td></tr><tr><td>Acinetobacter baumannii</td></tr><tr><td>Proteus vulgaris</td></tr><tr><td>Staphylococcus aureus</td></tr><tr><td>Ureplasma</td></tr><tr><td>Providencia stuartii</td></tr>
    </table>
    <svg class="corner" viewBox="0 0 696 260"><polygon points="0,7 480,260 0,141" fill="url(#facetTone)" role="img" aria-label="Low-poly blue facet texture"/><polygon points="0,141 479,260 0,260" fill="#1779c1"/></svg>
  </section>

  <!-- Wound / Sepsis -->
  <section class="page page--wound">
    <h2 class="page__title">WOUND/SEPSIS</h2>
    <p class="page__count">28 TARGETS</p>
    <p class="page__intro">A provider’s #1 priority is their patients. When you bring them more targets, you are providing them better tools for treatment.</p>
    <ul class="benefits">
      <li class="benefit"><svg><use href="#ico-dollar"/></svg>Cost effective to help maximize your lab’s profits</li>
      <li class="benefit"><svg><use href="#ico-timer"/></svg>&lt;45 minute run time ensures faster turnaround times</li>
      <li class="benefit"><svg><use href="#ico-gear"/></svg>Compatible with ALL PCR MACHINES</li>
      <li class="benefit"><svg><use href="#ico-chart"/></svg>Highly demanded targets to make your lab more appealing to providers</li>
    </ul>
    <table class="panel panel--tight" style="left:119px;top:349px;width:214px">
      <tr><th>FUNGI</th></tr>
      <tr><td>Candida krusei</td></tr><tr><td>Candida tropicalis</td></tr><tr><td>Candida glabrata</td></tr><tr><td>Candida parapsilosis</td></tr><tr><td>Candida albicans</td></tr><tr><td>Fusarium solani</td></tr><tr><td>Microsporum spp</td></tr><tr><td>Trichophyton spp</td></tr>
    </table>
    <table class="panel panel--tight" style="left:119px;top:540px;width:214px">
      <tr><th style="font-size:12.5px;letter-spacing:-.3px">ANTIMICROBIAL RESISTANCE</th></tr>
      <tr><td style="height:21px">Methicillin Resistance (MecA+C)</td></tr>
    </table>
    <table class="panel panel--tight" style="left:119px;top:601px;width:214px">
      <tr><th>VIRUSES</th></tr>
      <tr><td>Herpes Simplex Virus 1</td></tr><tr><td>Herpes Simplex Virus 2</td></tr>
    </table>
    <table class="panel panel--tight" style="left:364px;top:349px;width:214px">
      <tr><th>BACTERIA</th></tr>
      <tr><td>Escherichia coli</td></tr><tr><td>Streptococcus agalactiae</td></tr><tr><td>Klebsiella oxytoca</td></tr><tr><td>Staphylococcus saprophyticus</td></tr><tr><td>Pseudomonas aeruginosa</td></tr><tr><td>Staphylococcus haemolyticus</td></tr><tr><td>Enterococcus faecium</td></tr><tr><td>Enterococcus faecalis</td></tr><tr><td class="tall">Acinetobacter calcoaceticus-baumannii complex</td></tr><tr><td>Klebsiella aerogenes</td></tr><tr><td>Klebsiella pneumoniae</td></tr><tr><td>Staphylococcus aureus</td></tr><tr><td>Streptococcus pyogenes</td></tr><tr><td>Streptococcus pneumoniae</td></tr><tr><td>Streptococcus dysgalactiae</td></tr><tr><td>Staphylococcus lugdunensis</td></tr><tr><td>Staphylococcus epidermidis</td></tr>
    </table>
    <svg class="corner" viewBox="0 0 696 260"><polygon points="0,7 480,260 0,141" fill="url(#facetTone)" role="img" aria-label="Low-poly blue facet texture"/><polygon points="0,141 479,260 0,260" fill="#1779c1"/></svg>
  </section>

</main>
</body>
</html>
```